Business card needed for the Rydo of Dry Cleaning!

We need a slick business card design for a new company based out of Montreal called Casiers Plimo&Zet inc. (in French) and Plimo&Zet Lockers inc. (in English). We're the Rydo of Laundry. We offer services of dry cleaning, laundry (wash&fold), minor clothing alterations, shoe repair and parcel delivery through 24/7 secured and connected lockers. Ordres are placed through our mobile application. Real time notification are sent to customers when their order is ready for pickup. The lockers will be placed throughout the downtown area, in condo and office towers, where a high density of busy people converge. It is simple, user-friendly, and most importantly convenient. We're the out of the box dry cleaner, literally.

Target Market(s)

1) Professional workers wearing suits daily
2) Campus students living in residences
3) People using laundromats
4) Families with children/yuppies who prefer to use their time doing something else than laundry

Industry/Entity Type

Dry Cleaning

Contact Information for Business Card

Name / Annick-Solène Trudel
Title / CEO & Founder
Company Name / Casiers Plimo&Zet inc. | Plimo&Zet Lockers inc.
Website www.plimozet.ca

Requirements
Must have
• Text Logo: Plimo&Zet - Nettoyeurs 24/7 Cleaners
• Logo on one side and contact info on the other (bilingual)
• Minimalist, pure design
• "We care" for your belongings feeling
• Professional, technological, clean & fresh look
Should not have
• No busy visuals. No rainbow colors.

```html
<!DOCTYPE html>
<html lang="fr">
<head>
<meta charset="utf-8">
<title>Plimo&amp;Zet – Business Card</title>
<link rel="stylesheet" href="https://fonts.googleapis.com/css2?family=Montserrat:wght@400;500;600;700&display=swap">
<style>
  :root {
    --page: #e9e9ea;
    --card-black: #0b0b0c;
    --card-white: #ffffff;
    --accent: #29aae2;
    --ink: #1b1b1b;
    --grey: #6b6b6b;
    --light: #f2f2f2;
  }
  * { box-sizing: border-box; margin: 0; padding: 0; }
  html, body { width: 1200px; height: 913px; overflow: hidden; }
  body {
    background: var(--page);
    font-family: "Montserrat", Arial, sans-serif;
    position: relative;
  }
  .card {
    position: absolute;
    width: 520px;
    height: 297px;
    border-radius: 16px;
    overflow: hidden;
    box-shadow: 0 10px 28px rgba(0,0,0,.22);
    top: 308px;
    background: var(--card-black);
  }
  .card--contact { left: 50px; }
  .card--brand { left: 630px; }

  .card__wave { position: absolute; inset: 0; width: 100%; height: 100%; }

  .brand-name {
    position: absolute;
    font-weight: 600;
    line-height: 1;
    white-space: nowrap;
  }
  .descriptor {
    position: absolute;
    font-weight: 500;
    letter-spacing: .5px;
    white-space: nowrap;
  }

  .card--contact .brand-name { left: 150px; top: 34px; font-size: 36px; color: var(--ink); }
  .card--contact .descriptor { left: 152px; top: 74px; font-size: 10px; color: var(--grey); }

  .company-line {
    position: absolute;
    left: 96px; top: 98px;
    font-size: 10px;
    font-weight: 500;
    color: var(--ink);
    letter-spacing: .3px;
    white-space: nowrap;
  }

  .contacts {
    position: absolute;
    right: 24px; top: 150px;
    list-style: none;
    display: flex; flex-direction: column; gap: 6px;
  }
  .contacts li {
    display: flex; align-items: center; gap: 7px;
    color: var(--light); font-size: 10.5px;
  }
  .contacts svg { width: 10px; height: 10px; flex: none; }

  .person {
    position: absolute;
    left: 34px; top: 208px;
  }
  .person__name { color: #fff; font-weight: 600; font-size: 19px; white-space: nowrap; }
  .person__title { color: var(--accent); font-size: 11px; font-weight: 500; margin-top: 4px; padding-left: 118px; }

  .card--brand .brand-name { left: 0; right: 0; top: 96px; text-align: center; font-size: 50px; color: #fff; }
  .card--brand .descriptor { left: 0; right: 0; top: 156px; text-align: center; font-size: 13px; color: #d6d6d6; }

  .tagline {
    position: absolute;
    left: 0; right: 0; top: 222px;
    text-align: center;
    color: #fff; font-size: 12px; font-weight: 700; letter-spacing: .4px;
  }
  .tagline__accent { color: var(--accent); }
</style>
</head>
<body>

<section class="card card--contact" aria-label="Carte – coordonnées">
  <svg class="card__wave" viewBox="0 0 520 297" preserveAspectRatio="none" aria-hidden="true">
    <path d="M0 0 H520 V40 C440 120 270 180 0 190 Z" fill="#ffffff"/>
    <path d="M0 190 C270 180 440 120 520 40" fill="none" stroke="#29aae2" stroke-width="5"/>
  </svg>

  <p class="brand-name">Plimo&amp;Zet</p>
  <p class="descriptor">Nettoyeurs 24/7 Cleaners</p>

  <p class="company-line">CASIERS PLIMO&amp;ZET INC. - PLIMO&amp;ZET LOCKERS INC.</p>

  <ul class="contacts">
    <li><svg viewBox="0 0 10 10"><path fill="#29aae2" d="M2 0.5 L3.8 2.6 L2.8 3.8 C3.5 5.2 4.8 6.5 6.2 7.2 L7.4 6.2 L9.5 8 L8.2 9.5 C4.5 9.2 0.8 5.5 0.5 1.8 Z"/></svg>+1 514-555-0142</li>
    <li><svg viewBox="0 0 10 10"><path d="M0.5 2 H9.5 V8.5 H0.5 Z M1.3 2.6 L5 5.5 L8.7 2.6" stroke="#29aae2" stroke-width="1" fill="none"/></svg>www.plimozet.ca</li>
    <li><svg viewBox="0 0 10 10"><circle cx="5" cy="5" r="4.5" fill="#29aae2"/><path d="M0.5 5 H9.5 M5 0.5 C2.8 3 2.8 7 5 9.5 M5 0.5 C7.2 3 7.2 7 5 9.5" stroke="#0b0b0c" stroke-width=".8" fill="none"/></svg>info@annicktrudel.ca</li>
  </ul>

  <div class="person">
    <p class="person__name">Annick-Solène Trudel</p>
    <p class="person__title">CEO &amp; Founder</p>
  </div>
</section>

<section class="card card--brand" aria-label="Carte – nom">
  <p class="brand-name">Plimo&amp;Zet</p>
  <p class="descriptor">Nettoyeurs 24/7 Cleaners</p>
  <p class="tagline"><span class="tagline__accent">“WE CARE”</span> FOR YOUR BELONGINGS FEELING</p>
</section>

</body>
</html>
```